Modern Catering Company needs Letterhead Design

We need a letterhead design that will make effective use of the corporate logo and color scheme, along with careful typography, helps this letterhead design communicate the brand well. We do have a corporate logo, however feel free to enhance the color scheme with gold and purple. We are serving a very upscale clientele so the letterhead has to reflect elegance, professionalism, cleanliness, and modern style. We are branding the company so the letterhead and business cards must fit the brand story. There should be no cartoonish elements in the design and we are looking for sharper lines.

Target Market(s)

Businesses and upscale clientele

Industry/Entity Type

Catering

Contact Information for Business Card

while this design can have any number of quirks and distinctions, it needs to be cohesive with the entire brand story clean, professional but edgy

Requirements
Must have
• must have good and carefully placement of it’s logo and where you place the text or the message. Colors blue, very deep purple, jewel tones not pastels, gold. Blue must be the primary color you may accent with purple or gold. Contact information is as follows: Co-Owners/ Chefs: R. Hollowmere & L. Brandt, phone: 414-555-0182 email:Contact@orchardtablecatering.example, address: 6127 W Larkspur Hollow Rd, Milwaukee, WI 53299
Should not have
• pastel colors, Do not add the BBQ information to the letterhead or business card it was a mistake by the previous designer.

```html
<!DOCTYPE html>
<html lang="en">
<head>
<meta charset="utf-8">
<title>Orchard Table Catering — Letterhead</title>
<link rel="stylesheet" href="https://fonts.googleapis.com/css2?family=Open+Sans:wght@400;600&display=swap">
<style>
  :root {
    --brand-blue: #3a67b5;
    --ink: #2b2b2b;
    --ink-soft: #555a63;
    --paper: #ffffff;
    --backdrop: #e6e7e9;
    --watermark: #f0f1f3;
  }
  * { box-sizing: border-box; margin: 0; padding: 0; }
  html, body {
    width: 1200px; height: 1200px; overflow: hidden;
    background: var(--backdrop);
    font-family: "Open Sans", Arial, sans-serif;
  }
  .letterhead {
    position: absolute; left: 166px; top: 40px;
    width: 868px; height: 1120px;
    background: var(--paper);
    box-shadow: 0 6px 24px rgba(0,0,0,.12);
    overflow: hidden;
  }
  .brand-mark {
    position: absolute; left: 56px; top: 100px;
    display: flex; align-items: center; gap: 10px;
    width: 200px;
  }
  .brand-mark__dot {
    width: 14px; height: 14px; border-radius: 50%;
    background: var(--brand-blue); flex: none;
  }
  .brand-mark__name {
    font-size: 22px; font-weight: 400; color: var(--brand-blue);
    line-height: 1.15; letter-spacing: .3px;
  }
  .contact {
    position: absolute; right: 56px; top: 96px;
    display: flex; align-items: stretch; gap: 12px;
    font-size: 11.5px; color: var(--ink); line-height: 1.5;
  }
  .contact__address { text-align: right; padding-top: 6px; font-style: normal; }
  .contact__divider { width: 1px; background: var(--ink-soft); }
  .contact__lines { list-style: none; }
  .contact__lines li { display: flex; align-items: center; gap: 6px; }
  .contact__icon { width: 10px; height: 10px; flex: none; }
  .watermark {
    position: absolute; left: 0; top: 560px; width: 100%;
    text-align: center;
    font-size: 64px; font-weight: 400; color: var(--watermark);
    letter-spacing: 1px;
  }
  .footer-band {
    position: absolute; left: 0; bottom: 0;
    width: 100%; height: 88px;
  }
  .footer-band__name {
    position: absolute; right: 40px; bottom: 50px;
    font-size: 18px; color: var(--paper); letter-spacing: .5px;
  }
</style>
</head>
<body>
  <main class="letterhead">
    <header>
      <div class="brand-mark">
        <span class="brand-mark__dot"></span>
        <span class="brand-mark__name">Orchard Table<br>Catering</span>
      </div>
      <div class="contact">
        <address class="contact__address">
          Co-Owners / Chefs: R. Hollowmere &amp; L. Brandt<br>
          6127 W Larkspur Hollow Rd<br>
          Milwaukee, WI 53299
        </address>
        <span class="contact__divider"></span>
        <ul class="contact__lines">
          <li>
            <svg class="contact__icon" viewBox="0 0 12 12"><rect width="12" height="12" rx="2" fill="#3a67b5"/><path d="M3.5 3c.6 2.6 2.4 4.6 5 5.5l.8-1.2-1.4-.8-.6.6C6.3 6.6 5.4 5.7 5 4.7l.6-.6-.8-1.4z" fill="#fff"/></svg>
            414-555-0182
          </li>
          <li>
            <svg class="contact__icon" viewBox="0 0 12 12"><rect width="12" height="12" rx="2" fill="#3a67b5"/><path d="M3 3.5h6v5H3z" fill="none" stroke="#fff"/><path d="M3 3.5l3 2.5 3-2.5" fill="none" stroke="#fff"/></svg>
            Contact@orchardtablecatering.example
          </li>
        </ul>
      </div>
    </header>

    <div class="watermark" aria-hidden="true">Orchard Table Catering</div>

    <footer>
      <svg class="footer-band" viewBox="0 0 868 88" preserveAspectRatio="none" aria-hidden="true">
        <polygon points="0,46 560,46 560,0 868,0 868,88 0,88" fill="var(--brand-blue)"/>
      </svg>
      <span class="footer-band__name">Orchard Table Catering</span>
    </footer>
  </main>
</body>
</html>
```